A single page website & logo required for a Field Service Management Application

Name of the project - CrewTallo

We are software developers and we have a Field Service Management application ready. This software is all about optimizing the businesses that send their staff to various sites to provide service. Scheduling, creating jobs, quotes & invoices are a few salient features of it. It also has an accompanying Android & iPhone/iPad versions that will be used by the technicians.

More details can be provided, if needed.

After this web design project ends, the winning designer will be awarded the budget for the logo design through a 1on1 project.

Reason: I need to get the designs approved from my boss and he is currently overseas and is very busy. And hence I need the timeline to be extended.

Target Market(s)

All the Companies all over the world that send their staff to various sites to provide service.

Industry/Entity Type

Software

Logo Text

CrewTallo

Number of Pages Required

1 page

Font styles to use
Serif
Sans Serif

Requirements
Must have
• We would like to have the following components in the design:
• 1. Slider
• 2. Features of the software
• 3. Pricing Details
• 4. FAQs
• 5. Suitable for (Shows a list of all industries that our software is suitable for)
Nice to have
• A section with the background of a technician using our app on a mobile device (Screenshot can be provided)
Should not have
• Gaudy fonts and stereotypical designs

```html
<!DOCTYPE html>
<html lang="en">
<head>
<meta charset="utf-8">
<title>CrewTallo – Field Service Management</title>
<link rel="stylesheet" href="https://fonts.googleapis.com/css2?family=Raleway:wght@300;400;500;600;700;800&family=Open+Sans:wght@400;600&display=swap">
<style>
  :root {
    --white: #ffffff;
    --ink: #222222;
    --muted: #555555;
    --brand: #1a9ee6;
    --brand-dark: #16456f;
    --pricing-bg: #1ba2ec;
    --card-personal: #2eaef0;
    --card-personal-price: #52c4f8;
    --card-standard: #1a8fd8;
    --card-standard-price: #177fc2;
    --card-business: #1683c9;
    --card-business-price: #126ea9;
    --faq-bg: #ececec;
    --industry-top: #0d2f6e;
    --industry-bottom: #0a2457;
    --footer-bg: #06152e;
    --dot-active: #1c2f66;
  }
  * { box-sizing: border-box; margin: 0; padding: 0; }
  html, body { width: 1200px; height: 2250px; overflow: hidden; }
  body { font-family: "Raleway", Arial, sans-serif; color: var(--ink); background: var(--white); position: relative; }

  .site-header { height: 105px; position: relative; background: var(--white); }
  .brand { position: absolute; left: 204px; top: 36px; font-size: 25px; font-weight: 500; color: var(--brand); }
  .main-nav { position: absolute; left: 600px; top: 47px; display: flex; gap: 0; font-size: 14px; font-weight: 500; }
  .main-nav a { color: var(--ink); text-decoration: none; margin-right: 42px; }

  .hero { height: 528px; position: relative; overflow: hidden; }
  .hero-photo { position: absolute; inset: 0; background:
      radial-gradient(ellipse 260px 300px at 600px 330px, #9aa3ad 0%, rgba(120,130,140,0) 70%),
      radial-gradient(ellipse 300px 220px at 280px 460px, #c9cfd6 0%, rgba(200,205,210,0) 70%),
      linear-gradient(100deg, #3b3a3c 0%, #5c5b5e 35%, #6e6c6f 55%, #2f2e31 80%, #4a4a4d 100%); }
  .hero-text { position: absolute; left: 0; right: 0; text-align: center; color: var(--white); }
  .hero-title { top: 300px; font-size: 47px; font-weight: 800; letter-spacing: 0.5px; text-shadow: 0 2px 6px rgba(0,0,0,0.45); }
  .hero-subtitle { top: 358px; font-size: 27px; font-weight: 700; text-shadow: 0 2px 6px rgba(0,0,0,0.45); }
  .slider-dots { position: absolute; top: 593px; left: 556px; display: flex; gap: 5px; }
  .slider-dots span { width: 18px; height: 18px; border-radius: 50%; background: var(--white); display: block; }
  .slider-dots span.active { background: var(--dot-active); }

  .features { height: 396px; position: relative; text-align: center; }
  .section-title { font-weight: 400; font-size: 30px; }
  .features .section-title { position: absolute; top: 72px; left: 0; right: 0; color: #333; }
  .feature { position: absolute; top: 150px; width: 200px; text-align: center; }
  .feature-icon { display: block; margin: 0 auto; }
  .feature-name { font-size: 17px; font-weight: 500; margin-top: 12px; }
  .feature-text { font-size: 11px; line-height: 16.5px; color: var(--muted); margin-top: 6px; }

  .pricing { height: 385px; background: var(--pricing-bg); position: relative; color: var(--white); }
  .pricing .section-title { position: absolute; top: 40px; left: 0; right: 0; text-align: center; font-size: 29px; }
  .plan { position: absolute; top: 104px; width: 220px; height: 223px; text-align: center; }
  .plan-name { font-size: 21px; font-weight: 500; margin-top: 32px; letter-spacing: 0.5px; }
  .plan-text { font-size: 11px; line-height: 17px; padding: 8px 26px 0; }
  .plan-price { position: absolute; left: 0; right: 0; bottom: 0; height: 58px; line-height: 58px; font-family: "Open Sans", Arial, sans-serif; font-size: 29px; }
  .plan-price sup { font-size: 17px; vertical-align: 3px; }
  .plan-personal { left: 246px; background: var(--card-personal); }
  .plan-personal .plan-price { background: var(--card-personal-price); }
  .plan-standard { left: 491px; background: var(--card-standard); }
  .plan-standard .plan-price { background: var(--card-standard-price); }
  .plan-business { left: 736px; background: var(--card-business); }
  .plan-business .plan-price { background: var(--card-business-price); }

  .faq { height: 409px; background: var(--faq-bg); position: relative; }
  .faq .section-title { position: absolute; left: 204px; top: 58px; font-size: 30px; color: #333; }
  .faq-item { position: absolute; width: 260px; }
  .faq-question { font-size: 13.5px; line-height: 17px; color: #333; }
  .faq-answer { font-size: 10.5px; line-height: 17px; color: var(--muted); margin-top: 6px; }
  .faq-link { font-size: 11px; font-weight: 600; color: var(--ink); text-decoration: none; display: block; margin-top: 6px; }

  .industries { height: 305px; position: relative; color: var(--white); overflow: hidden; }
  .industries-photo { position: absolute; inset: 0; background:
      radial-gradient(ellipse 360px 200px at 640px 170px, rgba(70,120,200,0.55) 0%, rgba(70,120,200,0) 70%),
      linear-gradient(90deg, var(--industry-top) 0%, #153f8a 50%, var(--industry-bottom) 100%); }
  .industries .section-title { position: absolute; top: 50px; left: 0; right: 0; text-align: center; font-size: 29px; }
  .industry-list { position: absolute; top: 128px; list-style: none; }
  .industry-list li { font-size: 15px; height: 30px; display: flex; align-items: center; gap: 9px; }

  .site-footer { height: 122px; background: var(--footer-bg); position: relative; color: var(--white); }
  .footer-nav { position: absolute; left: 204px; top: 36px; display: flex; font-size: 13.5px; }
  .footer-nav a { color: var(--white); text-decoration: none; margin-right: 24px; }
  .copyright { position: absolute; left: 204px; top: 64px; font-size: 10px; color: #c8cfdc; }
  .social-links { position: absolute; left: 896px; top: 38px; display: flex; gap: 10px; }
  .social-links span { width: 16px; height: 16px; border-radius: 50%; background: var(--white); display: block; }
</style>
</head>
<body>

<header class="site-header">
  <div class="brand">CrewTallo</div>
  <nav class="main-nav">
    <a href="#about">About Us</a>
    <a href="#features">Features</a>
    <a href="#faq">FAQ</a>
    <a href="#pricing">Pricing</a>
    <a href="#contact">Contact</a>
  </nav>
</header>

<section class="hero">
  <div class="hero-photo" role="img" aria-label="Photo of a technician holding a smartphone running the app, with a tablet in the background"></div>
  <h1 class="hero-text hero-title">SED METUS AUGUE CONVALLIS</h1>
  <p class="hero-text hero-subtitle">SED METUS AUGUE CONVALLIS VEHICULA</p>
  <div class="slider-dots"><span class="active"></span><span></span><span></span><span></span></div>
</section>

<section class="features" id="features">
  <h2 class="section-title">Features of the software</h2>

  <div class="feature" style="left:251px">
    <svg class="feature-icon" width="92" height="100" viewBox="0 0 92 100">
      <polygon points="46,2 88,26 88,74 46,98 4,74 4,26" fill="#1a9ee6" stroke="#1a9ee6" stroke-width="6" stroke-linejoin="round"/>
      <rect x="30" y="36" width="32" height="28" rx="2" fill="none" stroke="#fff" stroke-width="3"/>
      <rect x="30" y="36" width="32" height="7" fill="#fff"/>
      <line x1="37" y1="31" x2="37" y2="39" stroke="#fff" stroke-width="3"/>
      <line x1="55" y1="31" x2="55" y2="39" stroke="#fff" stroke-width="3"/>
      <g fill="#fff"><rect x="35" y="47" width="5" height="4"/><rect x="44" y="47" width="5" height="4"/><rect x="53" y="47" width="5" height="4"/><rect x="35" y="55" width="5" height="4"/><rect x="44" y="55" width="5" height="4"/><rect x="53" y="55" width="5" height="4"/></g>
    </svg>
    <div class="feature-name">Scheduling</div>
    <p class="feature-text">Lorem ipsum dolor sit amet consectetuer adipiscing elit Nam cursus Morbi ut mi Nullam enim leo</p>
  </div>

  <div class="feature" style="left:498px">
    <svg class="feature-icon" width="92" height="100" viewBox="0 0 92 100">
      <polygon points="46,2 88,26 88,74 46,98 4,74 4,26" fill="#1a9ee6" stroke="#1a9ee6" stroke-width="6" stroke-linejoin="round"/>
      <rect x="31" y="37" width="30" height="21" rx="2" fill="none" stroke="#fff" stroke-width="3"/>
      <path d="M26 62 H66 L63 66 H29 Z" fill="#fff"/>
    </svg>
    <div class="feature-name">Creating Jobs</div>
    <p class="feature-text">Lorem ipsum dolor sit amet consectetuer adipiscing elit Nam cursus Morbi ut mi Nullam enim leo</p>
  </div>

  <div class="feature" style="left:746px">
    <svg class="feature-icon" width="92" height="100" viewBox="0 0 92 100">
      <polygon points="46,2 88,26 88,74 46,98 4,74 4,26" fill="#1a9ee6" stroke="#1a9ee6" stroke-width="6" stroke-linejoin="round"/>
      <path d="M32 42 H44 L48 46 V64 H32 Z" fill="none" stroke="#fff" stroke-width="2.5" stroke-linejoin="round"/>
      <path d="M42 34 H54 L60 40 V58 H48" fill="none" stroke="#fff" stroke-width="2.5" stroke-linejoin="round"/>
    </svg>
    <div class="feature-name">Quotes &amp; Invoices</div>
    <p class="feature-text">Lorem ipsum dolor sit amet consectetuer adipiscing elit Nam cursus Morbi ut mi Nullam enim leo</p>
  </div>
</section>

<section class="pricing" id="pricing">
  <h2 class="section-title">Pricing Details</h2>
  <div class="plan plan-personal">
    <h3 class="plan-name">PERSONAL</h3>
    <p class="plan-text">In massa libero interdum nec interdum vel blandit sed nulla In ullamcorper est eget tempor cursus neque mi consectetuer mi a ultricies massa est sed nisl Class apt</p>
    <div class="plan-price"><sup>$</sup>25.99</div>
  </div>
  <div class="plan plan-standard">
    <h3 class="plan-name">STANDARD</h3>
    <p class="plan-text">In massa libero interdum nec interdum vel blandit sed nulla In ullamcorper est eget tempor cursus neque mi consectetuer mi a ultricies massa est sed nisl Class apt</p>
    <div class="plan-price"><sup>$</sup>45.99</div>
  </div>
  <div class="plan plan-business">
    <h3 class="plan-name">BUSINESS</h3>
    <p class="plan-text">In massa libero interdum nec interdum vel blandit sed nulla In ullamcorper est eget tempor cursus neque mi consectetuer mi a ultricies massa est sed nisl Class apt</p>
    <div class="plan-price"><sup>$</sup>65.99</div>
  </div>
</section>

<section class="faq" id="faq">
  <h2 class="section-title">FAQ'S</h2>
  <div class="faq-item" style="left:204px;top:122px">
    <h3 class="faq-question">Interdum vel blandit sed nulla</h3>
    <p class="faq-answer">In ullamcorper est eget tempor cursus neque mi consectetuer mi a ultricies massa est sed nis</p>
    <a class="faq-link" href="#faq">Learn More</a>
  </div>
  <div class="faq-item" style="left:485px;top:122px">
    <h3 class="faq-question">Quisque dignissim congue leo</h3>
    <p class="faq-answer">In ullamcorper est eget tempor cursus neque mi consectetuer mi a ultricies massa</p>
    <a class="faq-link" href="#faq">Learn More</a>
  </div>
  <div class="faq-item" style="left:757px;top:122px">
    <h3 class="faq-question">Nullam enim leo egestas condimentum</h3>
    <p class="faq-answer">In ullamcorper est eget tempor cursus neque mi consectetuer mi a ultricies massa est sed</p>
    <a class="faq-link" href="#faq">Learn More</a>
  </div>
  <div class="faq-item" style="left:204px;top:252px">
    <h3 class="faq-question">Class aptent taciti sociosqu ad litora</h3>
    <p class="faq-answer">In ullamcorper est eget tempor cursus neque mi consectetuer mi a ultricies massa est sed nis</p>
    <a class="faq-link" href="#faq">Learn More</a>
  </div>
  <div class="faq-item" style="left:485px;top:252px">
    <h3 class="faq-question">Ut nisi erat fermentum vel congue</h3>
    <p class="faq-answer">In ullamcorper est eget tempor cursus neque mi consectetuer mi a ultricies massa</p>
    <a class="faq-link" href="#faq">Learn More</a>
  </div>
  <div class="faq-item" style="left:757px;top:252px;width:250px">
    <h3 class="faq-question">Nullam enim leo egestas id condimentum</h3>
    <p class="faq-answer">In ullamcorper est eget tempor cursus neque mi</p>
    <a class="faq-link" href="#faq">Learn More</a>
  </div>
</section>

<section class="industries">
  <div class="industries-photo" role="img" aria-label="Blue-tinted photo of hands using a tablet and phone at a work site"></div>
  <h2 class="section-title">Industries using our Software</h2>
  <ul class="industry-list" style="left:263px">
    <li><svg width="15" height="15" viewBox="0 0 16 16"><circle cx="8" cy="8" r="8" fill="#fff"/><path d="M4.5 8.3 L7 10.7 L11.5 5.7" fill="none" stroke="#0d2f6e" stroke-width="2"/></svg>Massa libero interdum</li>
    <li><svg width="15" height="15" viewBox="0 0 16 16"><circle cx="8" cy="8" r="8" fill="#fff"/><path d="M4.5 8.3 L7 10.7 L11.5 5.7" fill="none" stroke="#0d2f6e" stroke-width="2"/></svg>Aec interdum</li>
    <li><svg width="15" height="15" viewBox="0 0 16 16"><circle cx="8" cy="8" r="8" fill="#fff"/><path d="M4.5 8.3 L7 10.7 L11.5 5.7" fill="none" stroke="#0d2f6e" stroke-width="2"/></svg>Vel blandit sed</li>
  </ul>
  <ul class="industry-list" style="left:545px">
    <li><svg width="15" height="15" viewBox="0 0 16 16"><circle cx="8" cy="8" r="8" fill="#fff"/><path d="M4.5 8.3 L7 10.7 L11.5 5.7" fill="none" stroke="#0d2f6e" stroke-width="2"/></svg>Nulla In ullamcorper</li>
    <li><svg width="15" height="15" viewBox="0 0 16 16"><circle cx="8" cy="8" r="8" fill="#fff"/><path d="M4.5 8.3 L7 10.7 L11.5 5.7" fill="none" stroke="#0d2f6e" stroke-width="2"/></svg>Est eget tempor</li>
    <li><svg width="15" height="15" viewBox="0 0 16 16"><circle cx="8" cy="8" r="8" fill="#fff"/><path d="M4.5 8.3 L7 10.7 L11.5 5.7" fill="none" stroke="#0d2f6e" stroke-width="2"/></svg>Cursus neque</li>
  </ul>
  <ul class="industry-list" style="left:813px">
    <li><svg width="15" height="15" viewBox="0 0 16 16"><circle cx="8" cy="8" r="8" fill="#fff"/><path d="M4.5 8.3 L7 10.7 L11.5 5.7" fill="none" stroke="#0d2f6e" stroke-width="2"/></svg>Consectetuer</li>
    <li><svg width="15" height="15" viewBox="0 0 16 16"><circle cx="8" cy="8" r="8" fill="#fff"/><path d="M4.5 8.3 L7 10.7 L11.5 5.7" fill="none" stroke="#0d2f6e" stroke-width="2"/></svg>Aassa est sed</li>
    <li><svg width="15" height="15" viewBox="0 0 16 16"><circle cx="8" cy="8" r="8" fill="#fff"/><path d="M4.5 8.3 L7 10.7 L11.5 5.7" fill="none" stroke="#0d2f6e" stroke-width="2"/></svg>Nisl Class</li>
  </ul>
</section>

<footer class="site-footer" id="contact">
  <nav class="footer-nav">
    <a href="#home">Home</a>
    <a href="#about">About Us</a>
    <a href="#pricing">Pricing</a>
    <a href="#features">Features</a>
    <a href="#faq">FAQ</a>
    <a href="#contact">Contact</a>
  </nav>
  <p class="copyright">© 2015 Company Name&nbsp; All right reserved&nbsp; Term of Use</p>
  <div class="social-links" aria-label="Social media links">
    <span></span><span></span><span></span><span></span>
  </div>
</footer>

</body>
</html>
```